Looking for copywriting of the entire website + new selection of pictures

Hello,
My website's copy write is on the weaker side, so I'm looking for an entire re-do of my website's copy write. If you think a line is weak, re-write, otherwise you can leave it as is. We want our site to clearly explain what our events are, how they work, and why someone should sign up for them, while appealing to the hopeful, romantic, and nostalgic feelings of the visitors. Our speed dating events can be imagined as a modern day approach to the old-fashioned way of dating, where people got to know each other in person, away from the dating apps!! Additionally, I feel nearly all the existing pictures are rather weak, so please select entirely new pictures which give the website a less amateur feel, while retaining the playful nature of the brand. If there are areas where you think that section would benefit from no pictures at all, please communicate that.
Let me know if there are any further questions and thank you!
You can find the site at:
https://www.lanternmeetups.com
Industry/Entity Type
Speed Dating/Romance
Number of Pages Required
1 page
Look and feel
Each slider illustrates characteristics of the customer's brand and the style your logo design should communicate.

```html
<!DOCTYPE html>
<html lang="en">
<head>
<meta charset="utf-8">
<title>Lantern Meetups – Stop Swiping, Start Dating</title>
<link rel="stylesheet" href="https://fonts.googleapis.com/css2?family=Poppins:wght@300;400;500;600;700&display=swap">
<style>
:root{
  --pink:#f48fb5;
  --pink-strong:#f06a9e;
  --pink-soft:#fcc6d8;
  --blush:#fff4f8;
  --ink:#111111;
  --grey:#9a9a9a;
  --white:#ffffff;
  --black:#000000;
}
*{box-sizing:border-box;margin:0;padding:0}
html,body{width:1200px;height:3895px;overflow:hidden;background:var(--white)}
body{font-family:"Poppins",sans-serif;color:var(--ink);position:relative}
.page{position:relative;width:1200px;height:3895px;overflow:hidden}
.abs{position:absolute}

/* Hero */
.hero{left:0;top:0;width:1200px;height:640px;background:linear-gradient(100deg,#3a2a26 0%,#6b4a3c 30%,#c9977a 55%,#e6c0a4 75%,#a67a5f 100%)}
.hero-wave{left:0;top:560px;width:1200px;height:90px}
.brand{left:83px;top:55px;display:flex;align-items:center;gap:10px;color:var(--white);font-size:20px;font-weight:600}
.brand-dot{width:14px;height:14px;border-radius:50%;background:var(--white)}
.nav{left:446px;top:49px;display:flex;font-size:12px;font-weight:500;color:var(--white);letter-spacing:.3px}
.nav a{color:inherit;text-decoration:none;margin-right:31px}
.btn-contact{left:958px;top:38px;width:158px;height:36px;border-radius:18px;background:var(--white);display:flex;align-items:center;justify-content:center;gap:8px;font-size:12px;font-weight:600;color:var(--ink)}
.hero-eyebrow{left:83px;top:180px;color:var(--white);font-size:20px;font-weight:400}
.hero-title{left:81px;top:212px;color:var(--white);font-size:55px;font-weight:700;line-height:53px}
.hero-sub{left:83px;top:385px;color:var(--white);font-size:13px;line-height:20px;font-weight:300}
.btn-light{height:42px;border-radius:21px;display:flex;align-items:center;justify-content:center;font-size:16px;font-weight:500}
.btn-how{left:83px;top:466px;width:158px;background:var(--white);color:var(--ink)}
.btn-events{left:258px;top:466px;width:158px;border:1.5px solid var(--white);color:var(--white)}

/* How it works */
.how{left:0;top:640px;width:1200px;height:582px;background:var(--blush)}
.eyebrow{font-size:12px;font-weight:600;letter-spacing:1.5px;color:var(--pink-soft)}
.center{left:0;width:1200px;text-align:center}
.section-title{font-size:34px;font-weight:600;line-height:44px;color:var(--ink)}
.accent{color:var(--pink-soft)}
.rule{height:2px;background:#e8c9d3}
.step{width:206px;height:206px;border-radius:50%;background:var(--white);box-shadow:0 8px 24px rgba(240,106,158,.15);text-align:center}
.step-icon{position:absolute;left:73px;top:38px;width:60px;height:60px;border-radius:50%;background:var(--pink);display:flex;align-items:center;justify-content:center}
.step-text{position:absolute;left:40px;top:120px;width:126px;font-size:11px;line-height:17px;color:#555}

/* Events */
.events-title{left:83px;top:1298px;font-size:34px;font-weight:600}
.loc-photo{top:1390px;width:246px;height:342px;border-radius:12px}
.loc-label{top:1749px;font-size:15px;font-weight:400;color:var(--ink)}

/* Intro */
.intro{left:0;top:1840px;width:1200px;height:642px;background:var(--blush)}
.intro-body{left:83px;top:2076px;font-size:17px;line-height:25px;color:#444}
.btn-dark{left:83px;top:2235px;width:158px;height:40px;border-radius:20px;background:var(--black);color:var(--white);font-size:16px;font-weight:600;display:flex;align-items:center;justify-content:center}

/* Casual code */
.casual{left:0;top:2482px;width:1200px;height:581px;background:var(--pink-soft)}
.card{top:2652px;width:333px;height:351px;border-radius:20px;background:var(--white);padding:45px 22px 0 35px}
.card-icon{width:71px;height:71px;border-radius:12px;background:#f3f3f3;display:flex;align-items:center;justify-content:center}
.card-title{margin-top:26px;font-size:24px;font-weight:500;color:var(--ink);white-space:nowrap;line-height:32px}
.card-body{margin-top:18px;font-size:13px;line-height:20px;color:#b3b3b3;padding-right:10px}

/* CTA */
.cta{left:83px;top:3145px;width:1033px;height:208px;border-radius:22px;background:linear-gradient(90deg,#f48fb5,#fbc2d6)}
.cta-title{left:159px;top:40px;font-size:31px;font-weight:600;line-height:42px;color:var(--white)}
.cta-sub{left:159px;top:147px;font-size:13px;color:var(--white)}
.btn-join{left:717px;top:85px;width:158px;height:38px;border-radius:19px;background:var(--white);color:var(--pink-strong);font-size:13px;display:flex;align-items:center;justify-content:center}

/* Footer */
.footer-shape{left:0;top:3400px;width:1200px;height:495px}
.foot{color:var(--white)}
.foot-brand{left:83px;top:3603px;font-size:22px;font-weight:600;display:flex;align-items:center;gap:10px}
.foot-tag{left:83px;top:3660px;font-size:13px;line-height:20px}
.foot-copy{left:83px;top:3783px;font-size:13px;line-height:20px}
.foot-head{font-size:20px;font-weight:500}
.foot-rule{height:2px;background:#444;width:158px}
.foot-item{font-size:13px;line-height:20px;display:flex;align-items:center;gap:14px}
.ico-circle{width:32px;height:32px;border-radius:50%;background:var(--white);display:flex;align-items:center;justify-content:center;flex:none}
.ring{width:36px;height:36px;border-radius:50%;border:1.5px solid var(--white);flex:none}
.foot-link{font-size:16px;color:var(--white);text-decoration:none}
.social{font-size:17px;display:flex;align-items:center;gap:18px}
</style>
</head>
<body>
<div class="page">

  <!-- Hero -->
  <div class="abs hero" role="img" aria-label="Photo of a smiling woman holding hands with her date across a candlelit table"></div>
  <svg class="abs hero-wave" viewBox="0 0 1200 90" preserveAspectRatio="none" aria-hidden="true">
    <path d="M0 70 C150 20 280 20 420 45 C560 70 700 80 850 60 C1000 40 1100 40 1200 55 L1200 90 L0 90Z" fill="#fff4f8"/>
  </svg>

  <div class="abs brand"><span class="brand-dot"></span>Lantern Meetups</div>
  <nav class="abs nav"><a href="#">HOME</a><a href="#">EVENTS</a><a href="#">HOW IT WORKS</a><a href="#">FAQ</a></nav>
  <div class="abs btn-contact">
    <svg width="13" height="13" viewBox="0 0 24 24"><path d="M6.6 10.8a15 15 0 0 0 6.6 6.6l2.2-2.2a1 1 0 0 1 1-.25 11.4 11.4 0 0 0 3.6.57 1 1 0 0 1 1 1V20a1 1 0 0 1-1 1A17 17 0 0 1 3 4a1 1 0 0 1 1-1h3.5a1 1 0 0 1 1 1c0 1.25.2 2.45.57 3.57a1 1 0 0 1-.25 1z" fill="#111"/></svg>
    CONTACT US
  </div>

  <div class="abs hero-eyebrow">Lantern Meetups</div>
  <h1 class="abs hero-title">Stop Swiping,<br>Start Dating!</h1>
  <p class="abs hero-sub">Meet face to face, the way love used to begin.<br>Find an event near you and say hello in person.</p>
  <div class="abs btn-light btn-how">How It Works</div>
  <div class="abs btn-light btn-events">Our Events</div>

  <!-- How it works -->
  <section class="abs how"></section>
  <div class="abs center eyebrow" style="top:714px">HOW IT WORKS</div>
  <h2 class="abs center section-title" style="top:750px">No Hosts, No Name Tags - We Like To Keep<br>Things <span class="accent">Natural</span></h2>
  <div class="abs rule" style="left:533px;top:859px;width:134px"></div>

  <svg class="abs" style="left:0;top:880px" width="1200" height="280" aria-hidden="true">
    <g fill="none" stroke="#f8c3d5" stroke-width="1.5">
      <path d="M88 140 A129 129 0 0 1 345 140"/>
      <path d="M345 140 A129 129 0 0 0 602 140"/>
      <path d="M602 140 A129 129 0 0 1 859 140"/>
      <path d="M859 140 A129 129 0 0 0 1116 140"/>
    </g>
    <g fill="#f48fb5">
      <circle cx="88" cy="140" r="3"/><circle cx="345" cy="140" r="3"/><circle cx="602" cy="140" r="3"/><circle cx="859" cy="140" r="3"/><circle cx="1116" cy="140" r="3"/>
    </g>
  </svg>

  <div class="abs step" style="left:113px;top:915px">
    <div class="step-icon"><svg width="26" height="26" viewBox="0 0 24 24" fill="none" stroke="#fff" stroke-width="1.8"><path d="M12 21s7-6.5 7-12a7 7 0 0 0-14 0c0 5.5 7 12 7 12z"/><circle cx="12" cy="9" r="2.5"/></svg></div>
    <div class="step-text">Arrive At Your Chosen Time And Venue</div>
  </div>
  <div class="abs step" style="left:369px;top:915px">
    <div class="step-icon"><svg width="26" height="26" viewBox="0 0 24 24" fill="none" stroke="#fff" stroke-width="1.8"><path d="M4 4h16v12H8l-4 4z"/><path d="M8 8h8M8 12h6"/></svg></div>
    <div class="step-text">Your Personal Date Card Arrives By Text</div>
  </div>
  <div class="abs step" style="left:627px;top:915px">
    <div class="step-icon"><svg width="26" height="26" viewBox="0 0 24 24" fill="none" stroke="#fff" stroke-width="1.8"><path d="M3 4h13v9H7l-4 3z"/><path d="M16 8h5v10l-3-2h-8v-3"/></svg></div>
    <div class="step-text">Find Your Date, Pull Up A Seat, And Start Talking!</div>
  </div>
  <div class="abs step" style="left:884px;top:915px">
    <div class="step-icon"><svg width="26" height="26" viewBox="0 0 24 24" fill="none" stroke="#fff" stroke-width="1.8"><path d="M12 20s-8-4.8-8-10.5A4.5 4.5 0 0 1 12 7a4.5 4.5 0 0 1 8 2.5C20 15.2 12 20 12 20z"/></svg></div>
    <div class="step-text">Text Back A Match (M) Or A Pass (P) – We Do The Rest</div>
  </div>

  <!-- Event locations -->
  <h2 class="abs events-title">Event Locations</h2>
  <div class="abs loc-photo" style="left:83px;background:linear-gradient(160deg,#8fb6d3,#5a3a2e 60%,#c79a80)" role="img" aria-label="Photo of a couple embracing by the Boston waterfront"></div>
  <div class="abs loc-photo" style="left:346px;background:linear-gradient(180deg,#aebfcc,#6f8194 55%,#3f4b55)" role="img" aria-label="Photo of a suspension bridge over the river in Philadelphia"></div>
  <div class="abs loc-photo" style="left:608px;background:linear-gradient(180deg,#7ba6d6,#9fb6c9 40%,#5a4a44 70%,#8f7f74)" role="img" aria-label="Photo of a couple with coffee on the Jersey City waterfront"></div>
  <div class="abs loc-photo" style="left:871px;background:linear-gradient(180deg,#1d2530,#3b3f4c 50%,#b85a3a 80%,#2b2f38)" role="img" aria-label="Photo of a couple kissing under an umbrella on a rainy New York street"></div>
  <div class="abs loc-label" style="left:83px">BOSTON, MA</div>
  <div class="abs loc-label" style="left:346px">PHILADELPHIA, PA</div>
  <div class="abs loc-label" style="left:608px">JERSEY CITY, NJ</div>
  <div class="abs loc-label" style="left:871px">NEW YORK CITY, NY</div>

  <!-- Introduction -->
  <section class="abs intro"></section>
  <div class="abs eyebrow" style="left:83px;top:1975px">WHO WE ARE</div>
  <h2 class="abs section-title" style="left:83px;top:2003px">Introduction</h2>
  <div class="abs rule" style="left:83px;top:2060px;width:92px;background:#f4b7cb"></div>
  <p class="abs intro-body">Still single? 👋<br>Remember when people met over coffee, not apps?<br>Lantern Meetups brings that back.<br>Real tables, real smiles, real sparks.<br>Find an event near you and meet in person.</p>
  <div class="abs btn-dark">CONTACT US</div>
  <svg class="abs" style="left:520px;top:1895px" width="596" height="503" viewBox="0 0 596 503" role="img" aria-label="Photo of a couple sharing a tender moment in a rowboat">
    <defs><linearGradient id="blobFill" x1="0" y1="0" x2="1" y2="1"><stop offset="0" stop-color="#d9d4cc"/><stop offset=".45" stop-color="#4a4a3e"/><stop offset=".7" stop-color="#d7a33a"/><stop offset="1" stop-color="#8a7a62"/></linearGradient></defs>
    <path d="M175 40 C210 -10 300 -5 360 40 C420 85 440 130 500 170 C570 215 610 260 585 310 C560 360 470 330 410 380 C350 430 330 510 250 500 C170 490 210 410 150 370 C90 330 -10 330 2 280 C14 230 100 230 130 170 C155 120 140 90 175 40Z" fill="url(#blobFill)"/>
  </svg>

  <!-- Casual code -->
  <section class="abs casual"></section>
  <h2 class="abs center section-title" style="top:2514px">Embracing a Casual Code</h2>

  <article class="abs card" style="left:83px">
    <div class="card-icon"><svg width="30" height="30" viewBox="0 0 24 24" fill="none" stroke="#111" stroke-width="1.8"><path d="M12 6a2 2 0 1 1 2 2c-1 0-2 .8-2 2l9 6H3l9-6"/><path d="M5 16v4h14v-4"/></svg></div>
    <h3 class="card-title">Casual Dress</h3>
    <p class="card-body">Come as you are. No suits, no scripts, no pressure – just the easy charm of meeting someone new over a table, the way it used to happen before screens did the talking.</p>
  </article>
  <article class="abs card" style="left:433px">
    <div class="card-icon"><svg width="30" height="30" viewBox="0 0 24 24" fill="none" stroke="#111" stroke-width="1.8"><path d="M3 4h13v9H7l-4 3z"/><path d="M16 8h5v10l-3-2h-8v-3"/></svg></div>
    <h3 class="card-title">Casual Conversation</h3>
    <p class="card-body">Skip the small talk. Our playful prompts spark real conversation, so every short date feels warm and easy. Swap numbers later, only if you both say yes.</p>
  </article>
  <article class="abs card" style="left:783px">
    <div class="card-icon"><svg width="30" height="30" viewBox="0 0 24 24" fill="none" stroke="#111" stroke-width="1.8"><path d="M12 20s-8-4.8-8-10.5A4.5 4.5 0 0 1 12 7a4.5 4.5 0 0 1 8 2.5C20 15.2 12 20 12 20z"/></svg></div>
    <h3 class="card-title">Casual Dates</h3>
    <p class="card-body">No hosts, no bells, no endless swiping. Just find your table, spot your date and enjoy a light, hopeful conversation – the old-fashioned way, made for today.</p>
  </article>

  <!-- Call to action -->
  <div class="abs cta">
    <h2 class="abs cta-title">Our Events Fill Up Fast.<br>Don't Miss Out.</h2>
    <p class="abs cta-sub">Join our monthly newsletter to see every event before it sells out.</p>
    <div class="abs btn-join">Click To Join</div>
  </div>

  <!-- Footer -->
  <svg class="abs footer-shape" viewBox="0 0 1200 495" preserveAspectRatio="none" aria-hidden="true">
    <path d="M0 60 C200 -20 500 20 900 120 L0 130Z" fill="#f48fb5"/>
    <path d="M0 130 C250 60 600 150 900 120 C1050 105 1150 95 1200 90 L1200 495 L0 495Z" fill="#000"/>
  </svg>

  <div class="abs foot foot-brand"><span class="brand-dot"></span>Lantern Meetups</div>
  <p class="abs foot foot-tag">Meet face to face, the way love used to begin.<br>Find an event near you and say hello.</p>
  <p class="abs foot foot-copy">Copyright © 2023 Lantern Meetups.<br>All Rights Reserved.</p>

  <h3 class="abs foot foot-head" style="left:435px;top:3592px">Contact Us</h3>
  <div class="abs foot-rule" style="left:435px;top:3643px"></div>
  <div class="abs foot foot-item" style="left:435px;top:3667px">
    <span class="ico-circle"><svg width="16" height="16" viewBox="0 0 24 24"><path d="M12 22s7-7 7-13a7 7 0 0 0-14 0c0 6 7 13 7 13z" fill="#000"/><circle cx="12" cy="9" r="2.5" fill="#fff"/></svg></span>
    <span>88 Harbor Lane<br>Maple City, NY 10245</span>
  </div>
  <div class="abs foot foot-item" style="left:435px;top:3734px">
    <span class="ico-circle"><svg width="14" height="14" viewBox="0 0 24 24"><path d="M6.6 10.8a15 15 0 0 0 6.6 6.6l2.2-2.2a1 1 0 0 1 1-.25 11.4 11.4 0 0 0 3.6.57 1 1 0 0 1 1 1V20a1 1 0 0 1-1 1A17 17 0 0 1 3 4a1 1 0 0 1 1-1h3.5a1 1 0 0 1 1 1c0 1.25.2 2.45.57 3.57a1 1 0 0 1-.25 1z" fill="#000"/></svg></span>
    <span>(555) 310-4472</span>
  </div>
  <div class="abs foot foot-item" style="left:435px;top:3802px">
    <span class="ico-circle"><svg width="14" height="14" viewBox="0 0 24 24" fill="none" stroke="#000" stroke-width="2"><rect x="3" y="5" width="18" height="14" rx="2"/><path d="M3 7l9 6 9-6"/></svg></span>
    <span>welcome@lanternmeetups.com</span>
  </div>

  <h3 class="abs foot foot-head" style="left:697px;top:3592px">Quick Links</h3>
  <div class="abs foot-rule" style="left:697px;top:3643px"></div>
  <a class="abs foot-link" style="left:699px;top:3661px" href="#">Home</a>
  <a class="abs foot-link" style="left:699px;top:3695px" href="#">Events</a>
  <a class="abs foot-link" style="left:699px;top:3729px" href="#">How It Works</a>
  <a class="abs foot-link" style="left:699px;top:3763px" href="#">FAQ</a>

  <h3 class="abs foot foot-head" style="left:962px;top:3587px">Follow &nbsp;Us</h3>
  <div class="abs foot-rule" style="left:962px;top:3643px"></div>
  <div class="abs foot social" style="left:962px;top:3660px"><span class="ring"></span>Pictora</div>
  <div class="abs foot social" style="left:962px;top:3715px"><span class="ring"></span>Chirply</div>
  <div class="abs foot social" style="left:962px;top:3772px"><span class="ring"></span>Neighborly</div>

</div>
</body>
</html>
```